The Ladder of Mastery Customized for my Business

Hi! I am interested in getting some design ideas to take this Ladder of Mastery and put a bit of branding of my business into it. Open to any and all designs, this is intended to put on a 20"x24" or 16"x20" canvas so I can have it in my office for team training purposes. I have included a picture of the wall this canvas will go on. Thank you!

```html
<!DOCTYPE html>
<html lang="en">
<head>
<meta charset="utf-8">
<title>The Ladder of Mastery</title>
<link href="https://fonts.googleapis.com/css2?family=Oswald:wght@500&family=Barlow+Condensed:wght@500;600&family=Noto+Sans:wght@400;800&display=swap" rel="stylesheet">
<style>
  :root{
    --ink:#0d0d0d;
    --blue:#33ace3;
    --paper:#ffffff;
    --caption:#1a1a1a;
  }
  html,body{margin:0;padding:0;width:1200px;height:1200px;overflow:hidden;background:var(--paper);}
  .ladder{display:block;width:1200px;height:1200px;}
  .block{fill:var(--paper);}
  .grid-fill{fill:var(--blue);}
  .block-title{font-family:'Oswald',sans-serif;font-weight:500;font-size:30px;fill:var(--ink);text-anchor:middle;}
  .block-body{font-family:'Barlow Condensed',sans-serif;font-weight:500;font-size:14.5px;fill:var(--ink);text-anchor:middle;}
  .rail{fill:none;stroke:var(--ink);stroke-width:28;stroke-linecap:round;stroke-linejoin:round;}
  .frame{fill:none;stroke:var(--ink);stroke-width:10;stroke-linecap:round;stroke-linejoin:round;}
  .base-line{stroke:var(--ink);stroke-width:24;stroke-linecap:round;}
  .knob{fill:var(--ink);}
  .icon-spot{fill:var(--blue);}
  .virtue{font-family:'Oswald',sans-serif;font-weight:500;font-size:18px;fill:var(--ink);letter-spacing:.5px;text-anchor:middle;}
  .orbit{fill:none;stroke:var(--ink);stroke-width:1.6;}
  .caption{font-family:'Barlow Condensed',sans-serif;font-weight:600;font-size:13px;fill:var(--caption);text-anchor:middle;}
  .brand-name{font-family:'Barlow Condensed',sans-serif;font-weight:600;font-size:46px;fill:var(--blue);text-anchor:middle;}
  .banner{fill:var(--ink);}
  .title-light{font-family:'Noto Sans',sans-serif;font-weight:400;font-size:78px;fill:var(--paper);}
  .title-strong{font-family:'Noto Sans',sans-serif;font-weight:800;font-size:78px;fill:var(--blue);}
</style>
</head>
<body>
<svg class="ladder" viewBox="0 0 1920 1920" xmlns="http://www.w3.org/2000/svg" role="img" aria-label="The Ladder of Mastery">
  <defs>
    <clipPath id="ladder-interior">
      <polygon points="965,520 1515,1330 1515,1482 420,1482 420,1330"/>
    </clipPath>
    <path id="arc-left" d="M -55.4 32 A 64 64 0 0 1 32 -55.4"/>
    <path id="arc-right" d="M -32 -55.4 A 64 64 0 0 1 55.4 32"/>
  </defs>

  <g class="outer-frame">
    <path class="frame" d="M 945 490 Q 890 440 835 495 L 360 1195 Q 330 1250 418 1292"/>
    <path class="frame" d="M 985 490 Q 1040 440 1095 495 L 1570 1195 Q 1600 1250 1512 1292"/>
    <line class="base-line" x1="305" y1="1490" x2="1628" y2="1490"/>
  </g>

  <g class="block-grid" clip-path="url(#ladder-interior)">
    <polygon class="grid-fill" points="848,672 1082,672 1515,1318 1515,1482 420,1482 420,1318"/>
    <rect class="grid-fill" x="957" y="515" width="16" height="170"/>

    <rect class="block" x="876" y="690" width="180" height="142" rx="4"/>

    <rect class="block" x="700" y="850" width="58" height="146" rx="4"/>
    <rect class="block" x="770" y="850" width="190" height="146" rx="4"/>
    <rect class="block" x="975" y="850" width="190" height="146" rx="4"/>
    <rect class="block" x="1178" y="850" width="60" height="146" rx="4"/>

    <rect class="block" x="560" y="1010" width="92" height="150" rx="4"/>
    <rect class="block" x="665" y="1010" width="196" height="150" rx="4"/>
    <rect class="block" x="877" y="1010" width="178" height="150" rx="4"/>
    <rect class="block" x="1068" y="1010" width="202" height="150" rx="4"/>
    <rect class="block" x="1282" y="1010" width="120" height="150" rx="4"/>

    <rect class="block" x="440" y="1174" width="113" height="148" rx="4"/>
    <rect class="block" x="565" y="1174" width="195" height="148" rx="4"/>
    <rect class="block" x="772" y="1174" width="188" height="148" rx="4"/>
    <rect class="block" x="973" y="1174" width="190" height="148" rx="4"/>
    <rect class="block" x="1175" y="1174" width="197" height="148" rx="4"/>
    <rect class="block" x="1385" y="1174" width="125" height="148" rx="4"/>

    <rect class="block" x="443" y="1335" width="209" height="150" rx="4"/>
    <rect class="block" x="665" y="1335" width="200" height="150" rx="4"/>
    <rect class="block" x="877" y="1335" width="180" height="150" rx="4"/>
    <rect class="block" x="1070" y="1335" width="198" height="150" rx="4"/>
    <rect class="block" x="1280" y="1335" width="210" height="150" rx="4"/>
  </g>

  <g class="block-text">
    <text class="block-title" x="966" y="731" textLength="150" lengthAdjust="spacingAndGlyphs">COMPETITIVE</text>
    <text class="block-title" x="966" y="762" textLength="130" lengthAdjust="spacingAndGlyphs">GREATNESS</text>
    <text class="block-body" x="966" y="785"><tspan x="966">Be at our best when your</tspan><tspan x="966" dy="17">best is needed. Enjoyment of</tspan><tspan x="966" dy="17">a difficult challenge.</tspan></text>

    <text class="block-title" x="868" y="899">POISE</text>
    <text class="block-body" x="868" y="930"><tspan x="868">Just being yourself.</tspan><tspan x="868" dy="17">Being at ease in any situation.</tspan><tspan x="868" dy="17">Never fighting yourself.</tspan></text>

    <text class="block-title" x="1070" y="895" textLength="142" lengthAdjust="spacingAndGlyphs">CONFIDENCE</text>
    <text class="block-body" x="1070" y="926"><tspan x="1070">Respect without fear.</tspan><tspan x="1070" dy="17">May come from being prepared</tspan><tspan x="1070" dy="17">and keeping all things in</tspan><tspan x="1070" dy="17">proper perspective.</tspan></text>

    <text class="block-title" x="763" y="1054" textLength="128" lengthAdjust="spacingAndGlyphs">CONDITION</text>
    <text class="block-body" x="763" y="1077"><tspan x="763">Mental-Moral-Physical.</tspan><tspan x="763" dy="17">Rest, exercise and diet must be</tspan><tspan x="763" dy="17">considered. Moderation must be</tspan><tspan x="763" dy="17">practiced. Dissipation must be</tspan><tspan x="763" dy="17">eliminated.</tspan></text>

    <text class="block-title" x="966" y="1061">SKILL</text>
    <text class="block-body" x="966" y="1091"><tspan x="966">Knowledge of and the ability</tspan><tspan x="966" dy="17">to properly and quickly</tspan><tspan x="966" dy="17">execute the fundamentals.</tspan></text>

    <text class="block-title" x="1169" y="1059" textLength="144" lengthAdjust="spacingAndGlyphs">TEAM SPIRIT</text>
    <text class="block-body" x="1169" y="1085" textLength="184" lengthAdjust="spacingAndGlyphs">A genuine consideration for others.</text>
    <text class="block-body" x="1169" y="1102"><tspan x="1169">An eagerness to sacrifice personal</tspan><tspan x="1169" dy="17">interests of glory for the</tspan><tspan x="1169" dy="17">welfare of all.</tspan></text>

    <text class="block-title" x="662" y="1220" textLength="166" lengthAdjust="spacingAndGlyphs">SELF-CONTROL</text>
    <text class="block-body" x="662" y="1250"><tspan x="662">Practice self-discipline</tspan><tspan x="662" dy="17">and keep emotions under control.</tspan><tspan x="662" dy="17">Good judgment and common</tspan><tspan x="662" dy="17">sense are essential.</tspan></text>

    <text class="block-title" x="866" y="1222" textLength="128" lengthAdjust="spacingAndGlyphs">ALERTNESS</text>
    <text class="block-body" x="866" y="1254"><tspan x="866">Be at our best when your</tspan><tspan x="866" dy="17">best is needed. Enjoyment of</tspan><tspan x="866" dy="17">a difficult challenge.</tspan></text>

    <text class="block-title" x="1068" y="1220" textLength="112" lengthAdjust="spacingAndGlyphs">INITATIVE</text>
    <text class="block-body" x="1068" y="1250"><tspan x="1068">Cultivate the ability to make</tspan><tspan x="1068" dy="17">decisions and think alone.</tspan><tspan x="1068" dy="17">Do not be afraid of failure but,</tspan><tspan x="1068" dy="17">learn from it.</tspan></text>

    <text class="block-title" x="1273" y="1220" textLength="140" lengthAdjust="spacingAndGlyphs">INTENTNESS</text>
    <text class="block-body" x="1273" y="1248"><tspan x="1273">Set a realistic goal.</tspan><tspan x="1273" dy="17">Concentrate on its achievement</tspan><tspan x="1273" dy="17">by resisting all temptations and</tspan><tspan x="1273" dy="17">being determined and Persistant.</tspan></text>

    <text class="block-title" x="547" y="1388" textLength="176" lengthAdjust="spacingAndGlyphs">INDUSTRIOUSNESS</text>
    <text class="block-body" x="547" y="1420"><tspan x="547">There is no substitute for work.</tspan><tspan x="547" dy="17">Worthwhile results come from</tspan><tspan x="547" dy="17">hard work and careful planning.</tspan></text>

    <text class="block-title" x="765" y="1378" textLength="138" lengthAdjust="spacingAndGlyphs">FRIENDSHIP</text>
    <text class="block-body" x="765" y="1400"><tspan x="765">Comes from mutual esteem,</tspan><tspan x="765" dy="17">respect and devotion.</tspan><tspan x="765" dy="17">Like marriage it must not be taken</tspan><tspan x="765" dy="17">for granted but requires</tspan><tspan x="765" dy="17">a joint effort.</tspan></text>

    <text class="block-title" x="967" y="1386">LOYALTY</text>
    <text class="block-body" x="967" y="1418"><tspan x="967">To yourself and to all those</tspan><tspan x="967" dy="17">depending upon you.</tspan><tspan x="967" dy="17">Keep your self-respect.</tspan></text>

    <text class="block-title" x="1169" y="1380" textLength="150" lengthAdjust="spacingAndGlyphs">COOPERATION</text>
    <text class="block-body" x="1169" y="1408" textLength="176" lengthAdjust="spacingAndGlyphs">With all levels of your co-workers.</text>
    <text class="block-body" x="1169" y="1425">Listen if you want to be heard.</text>
    <text class="block-body" x="1169" y="1442" textLength="182" lengthAdjust="spacingAndGlyphs">Be interested in finding the best way,</text>
    <text class="block-body" x="1169" y="1459">not in having your own way.</text>

    <text class="block-title" x="1385" y="1382" textLength="150" lengthAdjust="spacingAndGlyphs">ENTHUSIASM</text>
    <text class="block-body" x="1385" y="1410"><tspan x="1385">Brushes off upon those with</tspan><tspan x="1385" dy="17">whom you come in contact.</tspan><tspan x="1385" dy="17">You must truly enjoy</tspan><tspan x="1385" dy="17">what you are doing.</tspan></text>
  </g>

  <g class="rails">
    <path class="rail" d="M 965 500 L 385 1360 L 312 1478"/>
    <path class="rail" d="M 965 500 L 1548 1360 L 1620 1478"/>
    <circle class="knob" cx="965" cy="505" r="16"/>
    <circle class="knob" cx="382" cy="1360" r="46"/>
    <circle class="knob" cx="1550" cy="1360" r="46"/>
  </g>

  <g class="virtue-left" transform="translate(897 594)">
    <text class="virtue"><textPath href="#arc-left" startOffset="50%">FAITH</textPath></text>
    <path class="orbit" d="M 36 -43 A 56 56 0 0 1 28 48.5"/>
    <circle class="knob" r="46"/>
    <circle class="icon-spot" r="24" role="img" aria-label="Icon: praying hands"/>
    <text class="caption" x="42" y="64"><tspan x="42">THROUGH</tspan><tspan x="42" dy="13">PRAYER</tspan></text>
  </g>
  <g class="virtue-left" transform="translate(787 748)">
    <text class="virtue"><textPath href="#arc-left" startOffset="50%">FIGHT</textPath></text>
    <path class="orbit" d="M 36 -43 A 56 56 0 0 1 28 48.5"/>
    <circle class="knob" r="46"/>
    <circle class="icon-spot" r="24" role="img" aria-label="Icon: boxing gloves"/>
    <text class="caption" x="44" y="64"><tspan x="44">DETERMINED</tspan><tspan x="44" dy="13">EFFORT</tspan></text>
  </g>
  <g class="virtue-left" transform="translate(690 900)">
    <text class="virtue"><textPath href="#arc-left" startOffset="50%">RESOURCEFULNESS</textPath></text>
    <path class="orbit" d="M 36 -43 A 56 56 0 0 1 28 48.5"/>
    <circle class="knob" r="46"/>
    <circle class="icon-spot" r="24" role="img" aria-label="Icon: hand with sparkles"/>
    <text class="caption" x="30" y="70"><tspan x="30">PROPER</tspan><tspan x="30" dy="13">JUDGMENT</tspan></text>
  </g>
  <g class="virtue-left" transform="translate(585 1053)">
    <text class="virtue"><textPath href="#arc-left" startOffset="50%">ADAPTABILITY</textPath></text>
    <path class="orbit" d="M 36 -43 A 56 56 0 0 1 28 48.5"/>
    <circle class="knob" r="46"/>
    <circle class="icon-spot" r="24" role="img" aria-label="Icon: head with shapes"/>
    <text class="caption" x="34" y="70"><tspan x="34">TO ANY</tspan><tspan x="34" dy="13">SITUATION</tspan></text>
  </g>
  <g class="virtue-left" transform="translate(483 1207)">
    <text class="virtue"><textPath href="#arc-left" startOffset="50%">AMBITION</textPath></text>
    <path class="orbit" d="M 36 -43 A 56 56 0 0 1 28 48.5"/>
    <circle class="knob" r="46"/>
    <circle class="icon-spot" r="24" role="img" aria-label="Icon: figure reaching for stars"/>
    <text class="caption" x="28" y="60"><tspan x="28">FOR</tspan><tspan x="28" dy="13">NOBLE</tspan><tspan x="28" dy="13">GOALS</tspan></text>
  </g>

  <g class="virtue-right" transform="translate(1035 593)">
    <text class="virtue"><textPath href="#arc-right" startOffset="50%">PATIENCE</textPath></text>
    <path class="orbit" d="M -36 -43 A 56 56 0 0 0 -28 48.5"/>
    <circle class="knob" r="46"/>
    <circle class="icon-spot" r="24" role="img" aria-label="Icon: head with clock"/>
    <text class="caption" x="-34" y="56"><tspan x="-34">GOOD</tspan><tspan x="-34" dy="13">THINGS</tspan><tspan x="-34" dy="13">TAKE TIME</tspan></text>
  </g>
  <g class="virtue-right" transform="translate(1140 748)">
    <text class="virtue"><textPath href="#arc-right" startOffset="50%">INTEGRITY</textPath></text>
    <path class="orbit" d="M -36 -43 A 56 56 0 0 0 -28 48.5"/>
    <circle class="knob" r="46"/>
    <circle class="icon-spot" r="24" role="img" aria-label="Icon: handshake over heart"/>
    <text class="caption" x="-36" y="64"><tspan x="-36">PURITY OF</tspan><tspan x="-36" dy="13">INTENTION</tspan></text>
  </g>
  <g class="virtue-right" transform="translate(1241 900)">
    <text class="virtue"><textPath href="#arc-right" startOffset="50%">RELIABILITY</textPath></text>
    <path class="orbit" d="M -36 -43 A 56 56 0 0 0 -28 48.5"/>
    <circle class="knob" r="46"/>
    <circle class="icon-spot" r="24" role="img" aria-label="Icon: shield with thumbs up"/>
    <text class="caption" x="-28" y="66"><tspan x="-28">CREATES</tspan><tspan x="-28" dy="13">RESPECT</tspan></text>
  </g>
  <g class="virtue-right" transform="translate(1343 1053)">
    <text class="virtue"><textPath href="#arc-right" startOffset="50%">HONESTY</textPath></text>
    <path class="orbit" d="M -36 -43 A 56 56 0 0 0 -28 48.5"/>
    <circle class="knob" r="46"/>
    <circle class="icon-spot" r="24" role="img" aria-label="Icon: raised hand on book"/>
    <text class="caption" x="-30" y="66"><tspan x="-30">IN THOUGHT</tspan><tspan x="-30" dy="13">AND</tspan><tspan x="-30" dy="13">ACTION</tspan></text>
  </g>
  <g class="virtue-right" transform="translate(1447 1207)">
    <text class="virtue"><textPath href="#arc-right" startOffset="50%">SINCERITY</textPath></text>
    <path class="orbit" d="M -36 -43 A 56 56 0 0 0 -28 48.5"/>
    <circle class="knob" r="46"/>
    <circle class="icon-spot" r="24" role="img" aria-label="Icon: person with hand on heart"/>
    <text class="caption" x="-20" y="70"><tspan x="-20">KEEPS</tspan><tspan x="-20" dy="13">FRIENDS</tspan></text>
  </g>

  <g class="brand-seal">
    <circle class="knob" cx="967" cy="330" r="132"/>
    <text class="brand-name" x="967" y="346">Harborline</text>
  </g>

  <g class="title-banner">
    <path class="banner" d="M 395 1505 H 1525 V 1600 Q 1525 1640 1485 1640 H 435 Q 395 1640 395 1600 Z"/>
    <text x="960" y="1600" text-anchor="middle"><tspan class="title-light">The Ladder </tspan><tspan class="title-strong">OF MASTERY</tspan></text>
  </g>
</svg>
</body>
</html>
```